Quiet Harbor Business Card
QH biz card design 1
Quiet Harbor Business Card - Funerals
Creative Brief
Simple
Marcus Pelley
2417 Linden Crossway, Ste 42 Glenmoor, OR 97199
marcus@quietharbr.com
www.quietharbr.com

```html
<!DOCTYPE html>
<html lang="en">
<head>
<meta charset="utf-8">
<title>Quiet Harbor Business Card</title>
<link rel="stylesheet" href="https://fonts.googleapis.com/css2?family=Arimo:wght@400;700&display=swap">
<style>
  :root {
    --backdrop: #e6e6e8;
    --card-white: #ffffff;
    --card-grey: #6f6f72;
    --accent-blue: #3d5fb3;
    --accent-blue-light: #8fa3d6;
    --ink-white: #ffffff;
    --ink-soft: #e4e4e6;
  }
  * { margin: 0; padding: 0; box-sizing: border-box; }
  html, body {
    width: 1200px;
    height: 802px;
    overflow: hidden;
    background: var(--backdrop);
    font-family: "Arimo", Arial, sans-serif;
  }
  .canvas { position: relative; width: 1200px; height: 802px; }
  .card {
    position: absolute;
    top: 252px;
    width: 520px;
    height: 297px;
    overflow: hidden;
    box-shadow: 0 10px 28px rgba(0, 0, 0, 0.18);
  }
  .card-front { left: 40px; background: var(--card-white); }
  .card-back { left: 640px; background: var(--card-grey); }
  .card-art { position: absolute; inset: 0; }

  .brand {
    position: absolute;
    display: flex;
    align-items: center;
    gap: 12px;
    font-weight: 700;
    text-transform: uppercase;
    letter-spacing: 1px;
    white-space: nowrap;
  }
  .brand-mark { width: 30px; height: 30px; border-radius: 50%; flex: none; }
  .brand-front { left: 40px; top: 62px; color: var(--accent-blue); font-size: 30px; }
  .brand-front .brand-mark { background: var(--accent-blue); }
  .brand-back {
    left: 50%;
    top: 50%;
    transform: translate(-50%, -50%);
    color: var(--ink-white);
    font-size: 30px;
  }
  .brand-back .brand-mark { background: var(--ink-white); }

  .contact-person { position: absolute; left: 40px; top: 196px; color: var(--ink-white); }
  .person-name {
    font-size: 16px;
    font-weight: 700;
    letter-spacing: 0.5px;
    text-transform: uppercase;
    margin-bottom: 8px;
  }
  .person-address { font-size: 12px; line-height: 1.45; color: var(--ink-soft); }

  .divider {
    position: absolute;
    left: 300px;
    top: 188px;
    width: 1px;
    height: 86px;
    background: var(--ink-soft);
    opacity: 0.7;
  }
  .contact-list {
    position: absolute;
    left: 316px;
    top: 186px;
    list-style: none;
    color: var(--ink-white);
    font-size: 11.5px;
  }
  .contact-list li { display: flex; align-items: center; gap: 8px; height: 22px; white-space: nowrap; }
  .contact-icon { width: 12px; height: 12px; flex: none; }
</style>
</head>
<body>
<main class="canvas">

  <section class="card card-front" aria-label="Business card front">
    <svg class="card-art" viewBox="0 0 520 297" preserveAspectRatio="none" aria-hidden="true">
      <path d="M0 168 C 160 160, 330 130, 520 92 L520 297 L0 297 Z" fill="var(--card-grey)"/>
      <path d="M0 160 C 160 152, 330 122, 520 84" fill="none" stroke="var(--accent-blue)" stroke-width="4"/>
      <path d="M0 152 C 160 144, 330 114, 520 76" fill="none" stroke="var(--accent-blue-light)" stroke-width="1.5"/>
    </svg>

    <div class="brand brand-front">
      <span class="brand-mark"></span>
      <span class="brand-name">Quiet Harbor</span>
    </div>

    <div class="contact-person">
      <p class="person-name">Marcus Pelley</p>
      <p class="person-address">2417 Linden Crossway, Ste 42<br>Glenmoor, OR 97199</p>
    </div>

    <div class="divider"></div>

    <ul class="contact-list">
      <li>
        <svg class="contact-icon" viewBox="0 0 12 12" aria-hidden="true"><rect x="3" y="0.5" width="6" height="11" rx="1.2" fill="none" stroke="#fff" stroke-width="1.2"/><circle cx="6" cy="9.5" r="0.7" fill="#fff"/></svg>
        <span>555-300-0190</span>
      </li>
      <li>
        <svg class="contact-icon" viewBox="0 0 12 12" aria-hidden="true"><path d="M2.5 1.5 L4.5 1.5 L5.5 4 L4.2 5 C5 6.6 5.6 7.2 7 7.8 L8 6.5 L10.5 7.5 L10.5 9.5 C6 10 2 6 2.5 1.5 Z" fill="#fff"/></svg>
        <span>555-800-0142</span>
      </li>
      <li>
        <svg class="contact-icon" viewBox="0 0 12 12" aria-hidden="true"><rect x="0.8" y="2.5" width="10.4" height="7" fill="none" stroke="#fff" stroke-width="1.1"/><path d="M1 3 L6 6.5 L11 3" fill="none" stroke="#fff" stroke-width="1.1"/></svg>
        <span>marcus@quietharbr.com</span>
      </li>
      <li>
        <svg class="contact-icon" viewBox="0 0 12 12" aria-hidden="true"><circle cx="6" cy="6" r="5" fill="none" stroke="#fff" stroke-width="1.1"/><ellipse cx="6" cy="6" rx="2.2" ry="5" fill="none" stroke="#fff" stroke-width="0.9"/><line x1="1" y1="6" x2="11" y2="6" stroke="#fff" stroke-width="0.9"/></svg>
        <span>www.quietharbr.com</span>
      </li>
    </ul>
  </section>

  <section class="card card-back" aria-label="Business card back">
    <div class="brand brand-back">
      <span class="brand-mark"></span>
      <span class="brand-name">Quiet Harbor</span>
    </div>
  </section>

</main>
</body>
</html>
```